Digital course framework design and style

We need a design for a framework to be used on an online course. The framework will have several layers and needs to have a style which can be followed throughout the course. The attached image is at the top level.

Need to keep to the triangle shape and the colour green and red for the words shown in the illustration. The three inner sections are pillars/pathways which we will expand out (Health, Adventure, Creativity) .
The course is Stuck to Striding (the inner section) so we need to show the flow from being frustrated with your kids on devices and not trying to be a successful and they can be, moving them to there kids taking action and frustration reducing. So important the framework has the feeling of progression and movement. The issue for each pillar/paths is the red text and the green being the result.

I want the framework to be simple to understand keeping to line diagram but introducing an icon for each piller/path. Needs to look professional and engaging.

I need to be able to edit the framework, present it elements so be in a format I can hide each Piller and display on a mouse click so layered.

Colours should fit into the brand colours

Core colour: #f07f37
Black secondary: #070707
Green : #0A633B
White: #FFFEFE

Website for brand approach: www.brightmovekids.example

Target Market(s)

Parents of children spending too long on devices

Font styles to use
Sans Serif

Requirements
Must have
• Clear and easy to see outcomes (green words on the example)
Flow from problem to solution (Stuck to Striding)
Style to be extended to further piller designs including icons for Health, Adventure, Creativity
Ability to present 1) the promise Stuck to Striding 2) each piller in turn
Brand colours included in brief
Should not have
• Busy complicated slide
Keep to line art not complex images

```html
<!DOCTYPE html>
<html lang="en">
<head>
<meta charset="utf-8">
<title>Stuck to Striding – Course Framework</title>
<link rel="stylesheet" href="https://fonts.googleapis.com/css2?family=Nunito:wght@800;900&family=Mulish:wght@300;400&display=swap">
<style>
  :root {
    --brand-orange: #f07f37;
    --brand-green: #0a633b;
    --brand-red: #e3131b;
    --brand-black: #070707;
    --brand-white: #fffefe;
    --issue-grey: #6d6e70;
  }
  html, body {
    margin: 0;
    padding: 0;
    width: 1200px;
    height: 1000px;
    overflow: hidden;
    background: var(--brand-orange);
  }
  .framework {
    display: block;
    width: 1200px;
    height: 1000px;
  }
  .stage-bg { fill: var(--brand-orange); }
  .ring { fill: var(--brand-white); stroke: var(--brand-black); stroke-width: 2; }
  .issue-band { fill: var(--issue-grey); }
  .pillar-band { fill: var(--brand-orange); }
  .core { fill: var(--brand-white); }
  .divider { stroke: var(--brand-white); stroke-width: 7; fill: none; }

  .outcome {
    font-family: "Nunito", sans-serif;
    font-weight: 900;
    font-size: 42px;
    fill: var(--brand-green);
    text-anchor: middle;
  }
  .issue {
    font-family: "Mulish", sans-serif;
    font-weight: 300;
    font-size: 22px;
    fill: var(--brand-white);
    text-anchor: middle;
    dominant-baseline: central;
  }
  .pillar-name {
    font-family: "Nunito", sans-serif;
    font-weight: 900;
    font-size: 36px;
    fill: var(--brand-white);
    text-anchor: middle;
    dominant-baseline: central;
  }
  .promise-goal {
    font-family: "Nunito", sans-serif;
    font-weight: 900;
    font-size: 40px;
    fill: var(--brand-green);
    text-anchor: middle;
  }
  .promise-start {
    font-family: "Nunito", sans-serif;
    font-weight: 900;
    font-size: 37px;
    fill: var(--brand-red);
    text-anchor: middle;
  }
  .icon-line { fill: none; stroke: var(--brand-white); stroke-width: 3; stroke-linecap: round; stroke-linejoin: round; }
  .icon-fill { fill: var(--brand-white); }
  .progress-arrow { fill: var(--brand-white); stroke: url(#progressGradient); stroke-width: 4; stroke-linejoin: round; }

  .brand-mark { fill: none; stroke: var(--brand-black); stroke-width: 3; }
  .brand-name {
    font-family: "Nunito", sans-serif;
    font-weight: 900;
    font-size: 22px;
    fill: var(--brand-black);
  }
</style>
</head>
<body>
<svg class="framework" viewBox="0 0 1200 1000" xmlns="http://www.w3.org/2000/svg" role="img" aria-label="Stuck to Striding framework with Health, Adventure and Creativity pillars">
  <defs>
    <linearGradient id="progressGradient" x1="0" y1="1" x2="0" y2="0">
      <stop offset="0" stop-color="#e3131b"/>
      <stop offset="1" stop-color="#2f9a3a"/>
    </linearGradient>
  </defs>

  <rect class="stage-bg" x="0" y="0" width="1200" height="1000"/>
  <circle class="ring" cx="600" cy="500" r="490"/>

  <!-- Issue layer -->
  <g class="layer-issues">
    <polygon class="issue-band" points="600,58 1002,735 198,735"/>
    <text class="issue" transform="translate(425,415) rotate(-59.4)" textLength="520" lengthAdjust="spacing">Anxious, Overweight, Unfit &amp; Disconnected</text>
    <text class="issue" transform="translate(765,410) rotate(59.4)" textLength="590" lengthAdjust="spacing">Unimaginative, negative, screen focused &amp; trapped</text>
    <text class="issue" x="600" y="700" textLength="378" lengthAdjust="spacing">Inactive, Insular, Solitary &amp; Timid</text>
  </g>

  <!-- Pillar layer -->
  <g class="layer-pillars">
    <polygon class="pillar-band" points="600,210 860,658 340,658"/>
    <polygon class="core" points="600,310 772,605 428,605"/>

    <g class="pillar pillar-health">
      <text class="pillar-name" transform="translate(512,413) rotate(-59.8)">HEALTH</text>
      <g class="icon-health" transform="translate(449,520) rotate(-59.8)">
        <polyline class="icon-line" points="-38,3 -26,3 -21,-7 -15,11 -10,3 -1,3"/>
        <path class="icon-fill" d="M2,-6 C2,-17 17,-19 18,-8 C19,-19 34,-17 34,-6 C34,5 24,11 18,18 C12,11 2,5 2,-6 Z"/>
      </g>
    </g>

    <g class="pillar pillar-creativity">
      <text class="pillar-name" transform="translate(728,480) rotate(59.8)">CREATIVITY</text>
      <g class="icon-creativity" transform="translate(649,345) rotate(59.8)">
        <path class="icon-line" d="M-18,2 C-20,-12 -6,-19 7,-16 C20,-13 23,-2 16,3 C11,7 6,5 6,11 C6,18 -14,18 -18,2 Z"/>
        <circle class="icon-fill" cx="-7" cy="-7" r="2.5"/>
        <circle class="icon-fill" cx="4" cy="-9" r="2.5"/>
        <line class="icon-line" x1="-3" y1="4" x2="-22" y2="-21"/>
      </g>
    </g>

    <g class="pillar pillar-adventure">
      <text class="pillar-name" x="555" y="633">ADVENTURE</text>
      <g class="icon-adventure" transform="translate(684,628)">
        <path class="icon-fill" d="M0,-6 a6,6 0 0 1 8,-6 a7,7 0 0 1 13,2 a5,5 0 0 1 1,10 h-20 a5,5 0 0 1 -2,-6 Z"/>
        <polyline class="icon-line" points="6,20 20,4 28,14 42,-6 60,20"/>
        <polyline class="icon-line" points="37,0 42,5 47,0"/>
      </g>
    </g>
  </g>

  <!-- Divider lines -->
  <g class="dividers">
    <line class="divider" x1="600" y1="58" x2="600" y2="312"/>
    <line class="divider" x1="428" y1="605" x2="205" y2="727"/>
    <line class="divider" x1="772" y1="605" x2="995" y2="727"/>
  </g>

  <!-- Promise: Stuck to Striding -->
  <g class="layer-promise">
    <text class="promise-goal" x="597" y="470">ACTION</text>
    <path class="progress-arrow" d="M600,486 L620,508 L610,508 L610,540 L590,540 L590,508 L580,508 Z"/>
    <text class="promise-start" x="597" y="587">FRUSTRATION</text>
  </g>

  <!-- Outcomes -->
  <g class="layer-outcomes">
    <g transform="translate(300,345) rotate(-59.4)">
      <text class="outcome" x="0" y="-8">Balanced, Fit,</text>
      <text class="outcome" x="0" y="40">Energetic &amp; Focused</text>
    </g>
    <g transform="translate(882,345) rotate(59.4)">
      <text class="outcome" x="0" y="-8">Bright, Idea Driven,</text>
      <text class="outcome" x="0" y="40">Positive &amp; Motivated</text>
    </g>
    <text class="outcome" x="600" y="812">Curious, Connected,</text>
    <text class="outcome" x="600" y="860">Excited &amp; Leading</text>
  </g>

  <!-- Brand name -->
  <g class="brand">
    <rect class="brand-mark" x="960" y="877" width="18" height="18"/>
    <text class="brand-name" x="986" y="894">Bright Move Kids</text>
  </g>
</svg>
</body>
</html>
```